Innovative Alcoholic Beverage Can Design

I need a can design for a beverage called "Zorvella". It is a beverage with 8% alcohol, classified as “ready-to-drink cocktail”. It is a drink with a feminine soul, developed for the young people (18-35 age) to be consumed in pubs and cool parties. It has an intense red color, similar to that of Brintolo. The flavor, called “velvet tide”, was made with exotic red fruits. The beverage will be available in 269 mL (9 us fl oz) cans. I need a can design that makes a big impact! Surprise me!

Zorvella / Cocktail / Velvet Tide / 269 mL / 8% ALC/VOL

```html
<!DOCTYPE html>
<html lang="en">
<head>
<meta charset="utf-8">
<title>Zorvella Cocktail – Velvet Tide</title>
<link href="https://fonts.googleapis.com/css2?family=Almendra:wght@400;700&family=Cinzel:wght@400&family=UnifrakturCook:wght@700&display=swap" rel="stylesheet">
<style>
  :root {
    --label-black: #111111;
    --label-black-edge: #1c1c1c;
    --brand-red: #e01a2b;
    --flavour-red: #d8141f;
    --silver: #a6a6a6;
    --fine-grey: #8c8c8c;
    --rose-bright: #ff2a2a;
    --rose-core: #c10f19;
    --rose-deep: #4a0307;
  }
  * { margin: 0; padding: 0; box-sizing: border-box; }
  html, body {
    width: 1200px;
    height: 1200px;
    overflow: hidden;
    background: var(--label-black);
  }
  .can-label {
    position: relative;
    width: 1200px;
    height: 1200px;
    background: linear-gradient(90deg, var(--label-black-edge) 0%, var(--label-black) 25%, var(--label-black) 75%, var(--label-black-edge) 100%);
    overflow: hidden;
  }
  .rose-visual {
    position: absolute;
    top: 330px;
    left: 170px;
    width: 760px;
    height: 640px;
  }
  .rose-visual svg { width: 100%; height: 100%; display: block; }
  .brand-name {
    position: absolute;
    top: 40px;
    left: 0;
    width: 1200px;
    text-align: center;
    font-family: "UnifrakturCook", serif;
    font-weight: 700;
    font-size: 250px;
    line-height: 1;
    color: var(--brand-red);
  }
  .product-type {
    position: absolute;
    top: 305px;
    right: 150px;
    font-family: "Almendra", serif;
    font-weight: 700;
    font-size: 92px;
    line-height: 1;
    color: var(--silver);
  }
  .flavour-name {
    position: absolute;
    top: 900px;
    left: 0;
    width: 1200px;
    text-align: center;
    font-family: "Almendra", serif;
    font-weight: 400;
    font-size: 150px;
    line-height: 1;
    color: var(--flavour-red);
  }
  .fine-print {
    position: absolute;
    top: 1110px;
    left: 0;
    width: 1200px;
    display: flex;
    justify-content: center;
    gap: 200px;
    font-family: "Cinzel", serif;
    font-size: 32px;
    color: var(--fine-grey);
    letter-spacing: 1px;
  }
</style>
</head>
<body>
  <main class="can-label">
    <div class="rose-visual" role="img" aria-label="Photograph of a glowing deep red rose in full bloom on black">
      <svg viewBox="0 0 760 640" aria-hidden="true">
        <defs>
          <radialGradient id="rose-glow" cx="58%" cy="48%" r="55%">
            <stop offset="0%" stop-color="var(--rose-bright)"/>
            <stop offset="30%" stop-color="var(--rose-core)"/>
            <stop offset="65%" stop-color="var(--rose-deep)"/>
            <stop offset="100%" stop-color="#111111" stop-opacity="0"/>
          </radialGradient>
          <filter id="soft-edge" x="-20%" y="-20%" width="140%" height="140%">
            <feGaussianBlur stdDeviation="22"/>
          </filter>
        </defs>
        <path filter="url(#soft-edge)" fill="url(#rose-glow)"
          d="M120 240 C150 140 260 70 380 80 C520 90 640 170 660 300 C680 430 600 560 460 590 C340 615 220 570 160 480 C110 400 95 320 120 240 Z"/>
      </svg>
    </div>
    <h1 class="brand-name">zorvella</h1>
    <p class="product-type">Cocktail</p>
    <h2 class="flavour-name">Velvet Tide</h2>
    <div class="fine-print">
      <span class="volume">269 ML</span>
      <span class="abv">8% ALC/VOL</span>
    </div>
  </main>
</body>
</html>
```